Book Cover (Front and Rear) for E book called Quiet Mazes

Create book cover front and rear book cover for e book called quiet mazes. Quiet Mazes is a book of 99 puzzles made up of Sudoku, word scrambles, word searches, cross words, mine finder.

Looking for a fairly simple cover similar to the attached 2 designs. Must mention title of book (quiet mazes) as well as making it clear that it is a book of puzzles and my name as the author (Hollis Varga). Rear cover basically same colour as front however just plain.

```html
<!DOCTYPE html>
<html lang="en">
<head>
<meta charset="utf-8">
<title>Quiet Mazes – Cover Spread</title>
<link href="https://fonts.googleapis.com/css2?family=Anton&family=Bebas+Neue&family=Inter:wght@400&family=Oswald:wght@300;500;600&family=Roboto+Condensed:wght@700&display=swap" rel="stylesheet">
<style>
  :root{
    --board-top:#ffffff;
    --board-mid:#e9e9eb;
    --cover-pink:#f9d0dc;
    --ink:#231f20;
    --plum:#7d4f8b;
    --lilac:#9b72c0;
    --white:#ffffff;
    --rule:#b99ad8;
  }
  *{margin:0;padding:0;box-sizing:border-box}
  html,body{width:1200px;height:1200px;overflow:hidden}
  body{
    position:relative;
    background:linear-gradient(180deg,var(--board-top) 0%,var(--board-mid) 45%,var(--board-mid) 60%,var(--board-top) 100%);
  }
  .board-label{
    position:absolute;top:86px;left:0;width:1200px;text-align:center;
    font-family:"Anton",sans-serif;font-size:146px;line-height:1;letter-spacing:6px;color:#000;
  }
  .spread{
    position:absolute;left:79px;top:305px;width:1041px;height:749px;
    background:var(--cover-pink);
    box-shadow:0 20px 60px rgba(0,0,0,.12);
    overflow:hidden;
  }
  /* back cover */
  .back-title{
    position:absolute;left:80px;top:44px;width:340px;text-align:center;
    font-family:"Anton",sans-serif;color:var(--white);line-height:.9;
  }
  .back-title span{display:block;font-size:72px}
  .back-sub{
    position:absolute;left:90px;top:190px;width:320px;text-align:center;
    font-family:"Bebas Neue",sans-serif;font-size:13px;line-height:1.1;color:var(--white);
  }
  .back-rule{
    position:absolute;left:90px;top:240px;width:320px;height:1px;
    background:linear-gradient(90deg,transparent,var(--rule) 30%,var(--rule) 70%,transparent);
  }
  .blurb{
    position:absolute;left:52px;top:263px;width:396px;text-align:center;
    font-family:"Inter",sans-serif;font-size:11.3px;line-height:17.4px;color:#111;
  }
  .blurb p{margin-bottom:17.4px}
  /* spine */
  .spine{
    position:absolute;left:499px;top:0;width:37px;height:749px;
  }
  .spine-main{
    position:absolute;left:29px;top:50px;transform-origin:0 0;transform:rotate(90deg);
    white-space:nowrap;display:flex;align-items:center;gap:10px;color:var(--ink);
  }
  .spine-title{font-family:"Roboto Condensed",sans-serif;font-size:20px;letter-spacing:.5px}
  .spine-bar{width:1px;height:18px;background:var(--ink);transform:rotate(90deg);margin:0 8px}
  .spine-sub{font-family:"Roboto Condensed",sans-serif;font-size:7.4px;line-height:1.25;letter-spacing:1.4px}
  .spine-author{
    position:absolute;left:27px;top:640px;transform-origin:0 0;transform:rotate(90deg);
    white-space:nowrap;font-family:"Oswald",sans-serif;font-weight:300;font-size:15px;color:var(--ink);
  }
  /* front cover */
  .front-title{
    position:absolute;left:586px;top:44px;width:421px;text-align:center;
    font-family:"Anton",sans-serif;line-height:.92;
  }
  .front-title .t-black{display:block;font-size:112px;color:var(--ink)}
  .front-title .t-plum{display:block;font-size:112px;color:var(--plum)}
  .front-sub{
    position:absolute;left:586px;top:266px;width:421px;text-align:center;
    font-family:"Bebas Neue",sans-serif;font-size:19px;line-height:1.1;color:var(--lilac);
  }
  .front-art{
    position:absolute;left:666px;top:360px;width:375px;height:245px;
    background:radial-gradient(ellipse at 45% 60%,#f6b9c5 0%,#f6c6d4 40%,rgba(249,208,220,0) 75%);
  }
  .front-author{
    position:absolute;left:586px;top:662px;width:421px;text-align:center;
    font-family:"Oswald",sans-serif;font-weight:600;font-size:42px;letter-spacing:10px;color:var(--plum);
  }
</style>
</head>
<body>
  <div class="board-label">COVER 2</div>

  <section class="spread">
    <div class="back-cover">
      <h2 class="back-title"><span>QUIET</span><span>MAZES</span></h2>
      <p class="back-sub">99 PUZZLES MADE UP OF SUDOKU, WORD SCRAMBLES, WORD SEARCHES, CROSS WORDS, MINE FINDER.</p>
      <div class="back-rule"></div>
      <div class="blurb">
        <p>Lorem ipsum dolor sit amet, consectetuer adipiscing elit, sed diam nonummy nibh euismod tincidunt ut laoreet dolore magna aliquam erat volutpat. Ut wisi enim ad minim veniam, quis nostrud exerci tation ullamcorper suscipit lobortis nisl ut aliquip ex ea commodo consequat. Duis autem vel eum iriure dolor in hendrerit in vulputate velit esse molestie consequat, vel illum dolore eu feugiat nulla facilisis at vero eros et accumsan et iusto odio dignissim qui blandit praesent luptatum zzril delenit augue duis dolore te feugait nulla facilisi.</p>
        <p>Lorem ipsum dolor sit amet, cons ectetuer adipiscing elit, sed diam nonummy nibh euismod tincidunt ut laoreet dolore magna aliquam erat volutpat. Ut wisi enim ad minim veniam, quis nostrud exerci tation ullamcorper suscipit lobortis nisl ut aliquip ex ea commodo consequat.</p>
        <p>Ut wisi enim ad minim veniam, quis nostrud exerci tation ullamcorper suscipit lobortis nisl ut aliquip ex ea commodo consequat.</p>
      </div>
    </div>

    <div class="spine">
      <div class="spine-main">
        <span class="spine-title">QUIET MAZES</span>
        <span class="spine-bar"></span>
        <span class="spine-sub">99 PUZZLES MADE UP OF SUDOKU, WORD SCRAMBLES,<br>WORD SEARCHES, CROSS WORDS, MINE FINDER.</span>
      </div>
      <div class="spine-author">HOLLIS VARGA</div>
    </div>

    <div class="front-cover">
      <h1 class="front-title"><span class="t-black">QUIET</span><span class="t-plum">MAZES</span></h1>
      <p class="front-sub">99 PUZZLES MADE UP OF SUDOKU, WORD SCRAMBLES, WORD<br>SEARCHES, CROSS WORDS, MINE FINDER.</p>
      <div class="front-art" role="img" aria-label="3D illustration of a hand in a blue sleeve placing a purple jigsaw piece beside three pink jigsaw pieces"></div>
      <div class="front-author">HOLLIS VARGA</div>
    </div>
  </section>
</body>
</html>
```